Homemaking training schools needs a Business Card design

Designer, Hello!

No special requirements, good-looking enough.
--------------------------------------------------------------------------

Name: Marcus Liao
Chairman
Tel: 0574-57418263
Mobile: 13852247106
Email: kelvory@mailpond.com
Web: www.tqb2031.com
Add: No.258, LinfengJie, DaoyueQu, Ningbo, Zhejiang

LOGO
Ningbo TQB Homemaking Training School

Target Market(s)

pregnant women, mothers, infants, the elderly and families, including cleaning, cooking, nursing training.

Industry/Entity Type

Business

Contact Information for Business Card

Name: Marcus Liao
Chairman
Tel: 0574-57418263
Mobile: 13852247106
Email: kelvory@mailpond.com
Web: www.tqb2031.com

LOGO

Font styles to use
Serif
Sans Serif
Decorative

Requirements
Nice to have
• Feels: clean, specifications, safety, comfort, warmth and happiness.

```html
<!DOCTYPE html>
<html lang="en">
<head>
<meta charset="utf-8">
<title>TianQiBao Business Card</title>
<link rel="stylesheet" href="https://fonts.googleapis.com/css2?family=Bebas+Neue&family=Open+Sans:wght@400;600&family=Quicksand:wght@400&display=swap">
<style>
  :root {
    --backdrop: #e9e6e2;
    --card: #2b2b2b;
    --accent-pink: #e6157f;
    --text-light: #ffffff;
    --text-soft: #d9d9d9;
  }
  * { box-sizing: border-box; margin: 0; padding: 0; }
  html, body { width: 1200px; height: 1000px; overflow: hidden; }
  body { background: var(--backdrop); position: relative; font-family: "Open Sans", sans-serif; }

  .card {
    position: absolute;
    left: 266px;
    width: 664px;
    background: var(--card);
    border-radius: 24px;
    box-shadow: 0 4px 12px rgba(0,0,0,0.25);
  }
  .card--front { top: 73px; height: 397px; }
  .card--back { top: 533px; height: 397px; }

  /* Front */
  .brand-name {
    position: absolute; left: 0; right: 0; top: 186px;
    text-align: center;
    font-family: "Open Sans", sans-serif; font-weight: 600;
    font-size: 58px; line-height: 1;
    color: var(--text-light);
  }
  .tagline {
    position: absolute; left: 131px; top: 254px; width: 404px;
    display: flex; align-items: center; gap: 8px;
    font-family: "Quicksand", sans-serif; font-size: 24px;
    color: var(--text-light); white-space: nowrap;
  }
  .tagline::before, .tagline::after {
    content: ""; flex: 1; height: 2px; background: var(--text-light);
  }
  .front-url {
    position: absolute; left: 0; right: 0; top: 350px;
    text-align: center; font-size: 16px; color: var(--text-soft);
  }

  /* Back */
  .person {
    position: absolute; right: 350px; top: 170px; text-align: right;
  }
  .person__name {
    font-family: "Bebas Neue", sans-serif; font-weight: 400; font-size: 36px; line-height: 1;
    color: var(--text-light); letter-spacing: 0.5px;
  }
  .person__role { font-size: 15px; color: var(--accent-pink); margin-top: 2px; }
  .divider {
    position: absolute; left: 332px; top: 152px; width: 2px; height: 89px;
    background: var(--text-light);
  }
  .contacts {
    position: absolute; left: 350px; top: 152px; list-style: none;
  }
  .contacts li {
    display: flex; align-items: center; gap: 6px;
    height: 22.5px; font-size: 16px; color: var(--text-light);
  }
  .contacts svg { width: 14px; height: 14px; fill: var(--accent-pink); flex: none; }
  .address {
    position: absolute; left: 0; right: 0; top: 346px;
    text-align: center; font-size: 17px; color: var(--text-light);
  }
</style>
</head>
<body>
  <section class="card card--front">
    <h1 class="brand-name">TianQiBao</h1>
    <p class="tagline">Training &amp; Services</p>
    <p class="front-url">www.tqb2031.com</p>
  </section>

  <section class="card card--back">
    <div class="person">
      <h2 class="person__name">MARCUS LIAO</h2>
      <p class="person__role">Chairman</p>
    </div>
    <span class="divider"></span>
    <ul class="contacts">
      <li>
        <svg viewBox="0 0 14 14" aria-hidden="true"><path d="M4 0h6a1 1 0 0 1 1 1v12a1 1 0 0 1-1 1H4a1 1 0 0 1-1-1V1a1 1 0 0 1 1-1zm0 2v9h6V2zm3 9.6a.8.8 0 1 0 0 1.6.8.8 0 0 0 0-1.6z"/></svg>
        0574-57418263
      </li>
      <li>
        <svg viewBox="0 0 14 14" aria-hidden="true"><path d="M1 4c0-1.5 2.5-2.5 6-2.5S13 2.5 13 4v1.5h-3V4H4v1.5H1zm2 3l2-2h4l2 2v5H3zm4 1a1.5 1.5 0 1 0 0 3 1.5 1.5 0 0 0 0-3z"/></svg>
        13852247106
      </li>
      <li>
        <svg viewBox="0 0 14 14" aria-hidden="true"><path d="M0 3h14v8H0zm1 1v.4l6 3.8 6-3.8V4z"/></svg>
        kelvory@mailpond.com
      </li>
      <li>
        <svg viewBox="0 0 14 14" aria-hidden="true"><path d="M7 0a7 7 0 1 1 0 14A7 7 0 0 1 7 0zm0 1.5a5.5 5.5 0 1 0 0 11 5.5 5.5 0 0 0 0-11zM3.5 5h7v1.3h-7zm0 2.7h7V9h-7zM6.3 2h1.4v10H6.3z"/></svg>
        www.tqb2031.com
      </li>
    </ul>
    <p class="address">No.258, LinfengJie, DaoyueQu, Ningbo, Zhejiang</p>
  </section>
</body>
</html>
```